Birchfall Kennels

create website page for Labrador Retriever stud dog business.

Target Market(s)

Owners looking to breed their dogs that compete in NFR/DSG hunt tests.

Industry/Entity Type

Dog Training

Logo Text

Birchfall Kennals - Stud Dogs

Number of Pages Required

1 page

Colors

Designer to choose colors to be used in the design.

Requirements
Must have
• link to or info from my dogs pedigree.
• Main dog I'm advertising. HRCH Pip's Whistle 4 Rounds MH
• http://www.fieldpupregistry.example/pedigree.asp?id=71926
• also link to gundog tallies-- for pass information.
• Can update the pictures to that actual pictures once design is complete.

```html
<!DOCTYPE html>
<html lang="en">
<head>
<meta charset="utf-8">
<title>Birchfall Kennels – Stud Dogs</title>
<link href="https://fonts.googleapis.com/css2?family=Raleway:wght@400;500;600;700&family=Open+Sans:wght@400;600&display=swap" rel="stylesheet">
<style>
:root{
  --yellow:#f3d40a;
  --blue:#1e9ad6;
  --ink:#222222;
  --text:#444444;
  --muted:#777777;
  --white:#ffffff;
}
*{box-sizing:border-box;margin:0;padding:0}
html,body{width:1200px;height:2486px;overflow:hidden;background:var(--white)}
body{position:relative;font-family:"Open Sans",Arial,sans-serif;color:var(--text)}
a{color:inherit;text-decoration:none}
.abs{position:absolute}

/* Header */
.site-header{position:absolute;left:0;top:0;width:1200px;height:103px;background:var(--white);box-shadow:0 2px 4px rgba(0,0,0,.08);z-index:5}
.brand{left:161px;top:20px;font-family:"Raleway",Arial,sans-serif;font-weight:700;font-size:30px;line-height:32px;color:var(--blue);width:200px}
.account-links{right:161px;top:22px;font-family:"Raleway",Arial,sans-serif;font-size:11px;font-weight:600;color:var(--blue);letter-spacing:.3px}
.account-links span{margin:0 8px}
.main-nav{right:161px;top:62px;display:flex;gap:29px;font-family:"Raleway",Arial,sans-serif;font-size:12.5px;font-weight:600;color:var(--ink)}
.main-nav .active{color:var(--blue)}

/* Hero */
.hero{left:0;top:103px;width:1200px;height:557px;overflow:hidden}
.hero-photo{position:absolute;inset:0;background:linear-gradient(120deg,#5d7a2e 0%,#6e8f3a 35%,#4a3226 55%,#c9b48a 75%,#9fb56a 100%)}
.hero-curve{position:absolute;left:0;top:0}
.hero-arrow{position:absolute;top:244px;width:44px;height:70px;background:rgba(255,255,255,.25)}
.hero-arrow.prev{left:0}
.hero-arrow.next{right:0}
.search{left:161px;top:126px;width:270px}
.search-title{font-family:"Raleway",Arial,sans-serif;font-weight:700;color:var(--white);font-size:22px;line-height:28px}
.search-title small{display:block;font-size:16px;line-height:24px}
.field{display:flex;height:31px;margin-top:13px;border:2px solid var(--white)}
.field:first-of-type{margin-top:20px}
.field label{width:88px;padding-left:8px;line-height:27px;font-family:"Raleway",Arial,sans-serif;font-weight:700;font-size:12.5px;color:var(--white);letter-spacing:.5px}
.field .select{flex:1;background:var(--white);font-size:11px;color:var(--muted);line-height:27px;padding-left:10px;position:relative}
.field .select::after{content:"";position:absolute;right:10px;top:11px;border:5px solid transparent;border-top-color:#555}
.buttons{display:flex;gap:6px;margin-top:16px}
.btn{height:36px;line-height:32px;padding:0 18px;font-family:"Raleway",Arial,sans-serif;font-weight:700;font-size:13px;color:var(--white);border:2px solid var(--white)}
.btn.submit{background:var(--blue);border-color:var(--blue)}

/* Section titles */
.section-title{left:0;width:1200px;text-align:center;font-family:"Raleway",Arial,sans-serif;font-weight:700;font-size:22px;color:var(--ink);letter-spacing:.3px}
.section-title em{font-style:normal;color:var(--blue)}

/* Featured */
.dog-card{top:769px;width:206px;text-align:center}
.dog-photo{height:227px;border:4px solid var(--yellow);background:linear-gradient(160deg,#8a7f68,#2a2622 50%,#a79d86)}
.dog-name{margin-top:18px;font-family:"Raleway",Arial,sans-serif;font-weight:600;font-size:17px;color:var(--blue);white-space:nowrap}
.dog-text{margin-top:8px;font-size:11px;line-height:19px;color:var(--text);padding:0 4px;height:57px}
.read-more{display:inline-block;margin-top:14px;width:101px;height:36px;line-height:32px;border:2px solid var(--blue);border-radius:18px;font-family:"Raleway",Arial,sans-serif;font-size:12px;font-weight:600;color:var(--blue)}

/* About */
.about{left:0;top:1196px;width:1200px;height:400px;overflow:hidden}
.about-photo{position:absolute;inset:0;background:linear-gradient(90deg,#556b24 0%,#7e8f30 30%,#b9ad38 60%,#e6c52a 80%,#f4e27a 100%)}
.about-curves{position:absolute;left:0;top:0}
.about-text{left:575px;top:126px;width:470px;color:var(--white)}
.about-text h2{font-family:"Raleway",Arial,sans-serif;font-weight:700;font-size:22px}
.about-text h3{margin-top:10px;font-family:"Raleway",Arial,sans-serif;font-weight:600;font-size:17px}
.about-text p{margin-top:10px;font-size:10px;line-height:16px}
.about-text a{text-decoration:underline}

/* FAQ */
.faq{width:420px;display:flex;gap:17px}
.faq-icon{flex:none;width:56px;height:56px;border:4px solid var(--yellow);border-radius:50%;text-align:center;line-height:48px;font-family:"Raleway",Arial,sans-serif;font-weight:700;font-size:19px;color:var(--yellow)}
.faq h4{font-family:"Raleway",Arial,sans-serif;font-weight:600;font-size:16px;color:var(--blue);margin-top:-3px;white-space:nowrap}
.faq p{margin-top:9px;font-size:11px;line-height:19px;color:var(--ink)}

/* Footer */
.footer-scene{left:0;top:2055px;width:1200px;height:155px;background:linear-gradient(180deg,rgba(30,154,214,0) 0%,rgba(30,154,214,0) 55%,var(--blue) 100%)}
.site-footer{left:0;top:2204px;width:1200px;height:282px;background:var(--blue);color:var(--white)}
.footer-col{top:56px}
.footer-col h5{font-family:"Raleway",Arial,sans-serif;font-weight:700;font-size:12.5px;letter-spacing:.3px}
.footer-col p{margin-top:18px;font-size:11px;line-height:19px}
.links{list-style:none;margin-top:14px;font-size:11px;line-height:22px}
.links li::before{content:"";display:inline-block;width:6px;height:6px;border-radius:50%;background:var(--yellow);margin-right:12px;vertical-align:1px}
.contact{list-style:none;margin-top:14px;font-size:11px;line-height:16px}
.contact li{display:flex;gap:12px;margin-bottom:10px}
.contact svg{flex:none;margin-top:1px}
.contact u{text-decoration:underline}
.socials{display:flex;gap:12px;margin-top:18px}
.socials a{width:38px;height:38px;border:3px solid var(--yellow);border-radius:50%;display:flex;align-items:center;justify-content:center}
.copyright{left:0;top:241px;width:1200px;text-align:center;font-size:10px}
</style>
</head>
<body>

<header class="site-header">
  <a class="brand abs" href="#">Birchfall Kennels</a>
  <div class="account-links abs"><a href="#">MY ACCOUNT</a><span>|</span><a href="#">LOGIN</a><span>|</span><a href="#">REGISTER</a></div>
  <nav class="main-nav abs">
    <a class="active" href="#">HOME</a><a href="#">ABOUT</a><a href="#">BREEDING</a><a href="#">LITTERS</a><a href="#">MEMBERS AREA</a><a href="#">RESOURCES</a><a href="#">CONTACT</a>
  </nav>
</header>

<section class="hero abs">
  <div class="hero-photo" role="img" aria-label="Photo of a chocolate and a yellow Labrador Retriever resting on grass"></div>
  <svg class="hero-curve" width="1200" height="557" viewBox="0 0 1200 557" aria-hidden="true">
    <path d="M0 0 H572 C490 140 470 390 590 557 H0 Z" fill="var(--yellow)"/>
  </svg>
  <div class="hero-arrow prev"><svg width="44" height="70" viewBox="0 0 44 70" aria-hidden="true"><path d="M27 22 L15 35 L27 48" fill="none" stroke="#fff" stroke-width="2"/></svg></div>
  <div class="hero-arrow next"><svg width="44" height="70" viewBox="0 0 44 70" aria-hidden="true"><path d="M17 22 L29 35 L17 48" fill="none" stroke="#fff" stroke-width="2"/></svg></div>
  <form class="search abs">
    <h1 class="search-title">SEARCH FOR<small>BIRCHFALL KENNELS LITTER</small></h1>
    <div class="field"><label>BREED:</label><div class="select">Birchfall Kennels</div></div>
    <div class="field"><label>LOCATION:</label><div class="select">Choose</div></div>
    <div class="field"><label>COLOR:</label><div class="select">Choose</div></div>
    <div class="buttons"><span class="btn submit">SUBMIT</span><span class="btn">RESET</span></div>
  </form>
</section>

<h2 class="section-title abs" style="top:708px">FEATURED <em>DOGS</em></h2>

<article class="dog-card abs" style="left:161px">
  <div class="dog-photo" role="img" aria-label="Photo of HRCH Pip's Whistle 4 Rounds MH running through water"></div>
  <h3 class="dog-name">HRCH Pip's Whistle</h3>
  <p class="dog-text">Our main stud dog, a proven hunt test retriever with steady marking and calm manners.</p>
  <a class="read-more" href="#">Read More</a>
</article>
<article class="dog-card abs" style="left:384px">
  <div class="dog-photo" role="img" aria-label="Photo of a black Labrador splashing through water"></div>
  <h3 class="dog-name">Full Pedigree</h3>
  <p class="dog-text">View his pedigree record online, with titled sires and dams from working field lines.</p>
  <a class="read-more" href="http://www.fieldpupregistry.example/pedigree.asp?id=71926">Read More</a>
</article>
<article class="dog-card abs" style="left:608px">
  <div class="dog-photo" role="img" aria-label="Photo of a black Labrador retrieving a pheasant"></div>
  <h3 class="dog-name">Gundog Tallies</h3>
  <p class="dog-text">See gundog tallies for pass information from each NFR and DSG hunt test he has run.</p>
  <a class="read-more" href="#">Read More</a>
</article>
<article class="dog-card abs" style="left:832px">
  <div class="dog-photo" role="img" aria-label="Photo of a black Labrador carrying a bird through water"></div>
  <h3 class="dog-name">Stud Services</h3>
  <p class="dog-text">Breeding terms, health clearances and booking details for owners planning a litter.</p>
  <a class="read-more" href="#">Read More</a>
</article>

<section class="about abs">
  <div class="about-photo" role="img" aria-label="Photo of a black Labrador lying in a sunlit field"></div>
  <svg class="about-curves" width="1200" height="400" viewBox="0 0 1200 400" aria-hidden="true">
    <path d="M0 0 H1200 V0 C900 60 400 40 0 12 Z" fill="var(--white)"/>
    <path d="M0 400 H1200 V340 C850 395 350 380 0 355 Z" fill="var(--white)"/>
  </svg>
  <div class="about-text abs">
    <h2>ABOUT BIRCHFALL KENNELS</h2>
    <h3>Stud Dog: HRCH Pip's Whistle 4 Rounds MH</h3>
    <p>Birchfall Kennels stands HRCH Pip's Whistle 4 Rounds MH at stud for owners whose dogs compete in NFR and DSG hunt tests. View his full pedigree at <a href="http://www.fieldpupregistry.example/pedigree.asp?id=71926">http://www.fieldpupregistry.example/pedigree.asp?id=71926</a> and check <a href="#">gundog tallies</a> for his pass information. He brings proven marking, steady line manners and a calm kennel temperament to every litter.</p>
  </div>
</section>

<h2 class="section-title abs" style="top:1630px">FREQUENTLY ASKED <em>QUESTIONS</em></h2>

<div class="faq abs" style="left:161px;top:1708px">
  <div class="faq-icon">Q</div>
  <div><h4>What's the purpose of Birchfall Kennels?</h4><p>The purpose of Birchfall Kennels is to provide working and Birchfall Kennels owners an educational and resourceful research pedigree database.</p></div>
</div>
<div class="faq abs" style="left:628px;top:1708px">
  <div class="faq-icon">Q</div>
  <div><h4>Why are their only certain breeds on this site?</h4><p>The administer and creator of this site hereby disclaim any liability for the accuracy or meaning of any such information provided in the site. Users hereby agree to use or rely on such information.</p></div>
</div>
<div class="faq abs" style="left:161px;top:1827px">
  <div class="faq-icon">Q</div>
  <div><h4>What are the terms of Birchfall Kennels?</h4><p>The purpose of Birchfall Kennels is to provide working and Birchfall Kennels owners an educational and resourceful research pedigree database.</p></div>
</div>
<div class="faq abs" style="left:628px;top:1827px">
  <div class="faq-icon">Q</div>
  <div><h4>How do I add a Birchfall Kennels name?</h4><p>It's also a way to test a breeding out by looking at each pedigrees together.&nbsp; It's not a real litter, but just gives you a picture of what the breeding will look like.</p></div>
</div>
<div class="faq abs" style="left:161px;top:1946px">
  <div class="faq-icon">Q</div>
  <div><h4>what can i do when I see a duplicated dog?</h4><p>To add a dog, start by searching for them. (search for dog's WITHOUT titles)&nbsp; Titles are any prefix or suffix title around the registered name. If you are unable to find your dog's.</p></div>
</div>
<div class="faq abs" style="left:628px;top:1946px">
  <div class="faq-icon">Q</div>
  <div><h4>May I add my Birchfall Kennels?</h4><p>Birchfall Kennels has created precautions to prevent duplicate entries, but sometimes duplicate dog's will be entered.&nbsp; The most common reasons are misspelling.</p></div>
</div>

<div class="footer-scene abs" role="img" aria-label="Illustration of a person walking dogs across grass, in blue silhouette"></div>

<footer class="site-footer abs">
  <div class="footer-col abs" style="left:161px;width:230px">
    <h5>ABOUT US</h5>
    <p>Stud services for working Labrador owners. HRCH Pip's Whistle 4 Rounds MH, proven in NFR and DSG hunt tests, with pedigree and pass records online.</p>
  </div>
  <div class="footer-col abs" style="left:421px;width:160px">
    <h5>USEFUL LINKS</h5>
    <ul class="links"><li>Privacy policy</li><li>Cookie policy</li><li>Terms &amp; Conditions</li><li>Blog</li><li>Contact us</li></ul>
  </div>
  <div class="footer-col abs" style="left:610px;width:220px">
    <h5>CONTACT US</h5>
    <ul class="contact">
      <li><svg width="13" height="13" viewBox="0 0 13 13" aria-hidden="true"><path d="M3 1 L5 4 L4 5.5 C5 7.5 5.5 8 7.5 9 L9 8 L12 10 L10.5 12 C5.5 11.5 1.5 7.5 1 2.5 Z" fill="var(--yellow)"/></svg>03 5550 0148 (Phone)</li>
      <li><svg width="13" height="13" viewBox="0 0 13 13" aria-hidden="true"><rect x="3" y="1" width="7" height="4" fill="var(--yellow)"/><rect x="1" y="5" width="11" height="5" rx="1" fill="var(--yellow)"/><rect x="3" y="9" width="7" height="3" fill="var(--yellow)"/></svg>03 5550 0148&nbsp; (Fax)</li>
      <li><svg width="13" height="13" viewBox="0 0 13 13" aria-hidden="true"><rect x="1" y="3" width="11" height="8" fill="var(--yellow)"/><path d="M1 3 L6.5 7.5 L12 3" fill="none" stroke="var(--blue)" stroke-width="1.2"/></svg><u>admin@BirchfallKennels.com</u></li>
      <li><svg width="13" height="13" viewBox="0 0 13 13" aria-hidden="true"><path d="M6.5 1 C4 1 2.5 3 2.5 5 C2.5 8 6.5 12 6.5 12 C6.5 12 10.5 8 10.5 5 C10.5 3 9 1 6.5 1 Z" fill="var(--yellow)"/><circle cx="6.5" cy="5" r="1.5" fill="var(--blue)"/></svg>PO Box: 4417, Thailand<br>lorem si2710</li>
    </ul>
  </div>
  <div class="footer-col abs" style="left:857px;width:190px">
    <h5>CONNECT WITH US</h5>
    <p>Follow the kennel for litter news and hunt test results.</p>
    <div class="socials">
      <a href="#" aria-label="Email"><svg width="16" height="12" viewBox="0 0 16 12" aria-hidden="true"><rect x="0.5" y="0.5" width="15" height="11" fill="none" stroke="#fff" stroke-width="1.4"/><path d="M1 1 L8 7 L15 1" fill="none" stroke="#fff" stroke-width="1.4"/></svg></a>
      <a href="#" aria-label="Message"><svg width="16" height="14" viewBox="0 0 16 14" aria-hidden="true"><path d="M1 1 H15 V10 H6 L2 13 V10 H1 Z" fill="none" stroke="#fff" stroke-width="1.4" stroke-linejoin="round"/></svg></a>
      <a href="#" aria-label="Share"><svg width="16" height="16" viewBox="0 0 16 16" aria-hidden="true"><circle cx="3" cy="8" r="2" fill="#fff"/><circle cx="13" cy="3" r="2" fill="#fff"/><circle cx="13" cy="13" r="2" fill="#fff"/><path d="M3 8 L13 3 M3 8 L13 13" stroke="#fff" stroke-width="1.4"/></svg></a>
      <a href="#" aria-label="Phone"><svg width="14" height="14" viewBox="0 0 13 13" aria-hidden="true"><path d="M3 1 L5 4 L4 5.5 C5 7.5 5.5 8 7.5 9 L9 8 L12 10 L10.5 12 C5.5 11.5 1.5 7.5 1 2.5 Z" fill="#fff"/></svg></a>
    </div>
  </div>
  <p class="copyright abs">© Copyright 2017. Birchfall Kennels. All Rights ReservedPrivacy Policy And Terms and Conditions</p>
</footer>

</body>
</html>
```